Non-fiction book about abuse and survival, needs cover design

This book is about me, and a lifetime of abuse that I survived. The goal is to help others in abusive situations break the cycle of shame that accompanies unhealthy and toxic relationships. I want the cover to illustrate a vast and sometimes scary world where we victims feel alone. It's up to us to choose our destiny, and sometimes we must do that when others don't agree. But there is hope. No longer do we need to believe the lie that something broken is better than nothing at all. After reading this, others will learn to trust their intuition, and how to avoid the pitfalls and red flags of toxic relationships. I want the cover to also show strength, hope, and positivity in the face of adversity. The picture of me (attached) is a good start to show a great big and sometimes frightening world a victim of abuse lives in. I love nature photos, but it's not a requirement for this project. I prefer simple designs. Thank you so much!

Target Market(s)

Survivors of abuse, at risk youth, and friends/family with loved ones who are abused

Requirements
Must have
• Title: The Lantern Keeper
Subtitle: Leave the Crooked Road That Runs Past Every Open Gate You Were Shown
Nice to have
• Outdoor scenery, open spaces.

```html
<!DOCTYPE html>
<html lang="en">
<head>
<meta charset="utf-8">
<title>The Lantern Keeper — Cover Spread</title>
<link rel="stylesheet" href="https://fonts.googleapis.com/css2?family=Bebas+Neue&family=Oswald:wght@500;600&family=Mulish:ital,wght@1,500&family=Libre+Baskerville&display=swap">
<style>
  :root {
    --page: #f2f2f2;
    --night: #07080c;
    --night-rock: #3a2418;
    --sky: #2f5fae;
    --sky-light: #7d9fd0;
    --rock: #a8502a;
    --rock-dark: #6b2e17;
    --sand: #b5582a;
    --sand-dark: #7a3517;
    --paper: #ffffff;
    --ink: #111111;
  }
  * { box-sizing: border-box; margin: 0; padding: 0; }
  html, body { width: 899px; height: 1200px; overflow: hidden; background: var(--page); }
  .spread {
    position: absolute; left: 14px; top: 298px;
    width: 870px; height: 603px;
    display: flex;
    box-shadow: 0 6px 20px rgba(0,0,0,.18);
  }
  /* Back cover */
  .back {
    position: relative; width: 402px; height: 100%;
    overflow: hidden; background: var(--night);
  }
  .back-scene {
    position: absolute; inset: 0;
    background:
      radial-gradient(ellipse 70% 90% at 100% 55%, rgba(90,48,28,.75), rgba(58,36,24,.35) 55%, transparent 80%),
      linear-gradient(90deg, var(--night) 45%, var(--night-rock) 100%);
  }
  .back-title {
    position: absolute; left: 30px; top: 22px;
    font-family: "Bebas Neue", sans-serif; font-weight: 400; color: var(--paper);
    line-height: .86; text-shadow: 2px 3px 0 rgba(0,0,0,.35);
  }
  .back-title .t1 { display: block; font-size: 56px; }
  .back-title .t2 { display: block; font-size: 80px; }
  .back-title .t3 { display: block; font-size: 104px; }
  .blurb-disc {
    position: absolute; left: 48px; top: 192px;
    width: 306px; height: 306px; border-radius: 50%;
    background: var(--paper);
    display: flex; align-items: flex-start; justify-content: center;
    padding-top: 34px;
  }
  .blurb {
    font-family: "Libre Baskerville", serif; font-size: 9.4px;
    line-height: 1.42; color: var(--ink); text-align: center;
  }
  /* Spine */
  .spine {
    position: relative; width: 67px; height: 100%;
    background: var(--paper);
    display: flex; flex-direction: column; align-items: center;
    padding-top: 46px;
  }
  .spine-title {
    writing-mode: vertical-rl;
    font-family: "Oswald", sans-serif; font-weight: 600;
    font-size: 25px; letter-spacing: 9px; color: var(--ink);
  }
  .spine-author {
    writing-mode: vertical-rl; margin-top: auto; margin-bottom: 68px;
    font-family: "Oswald", sans-serif; font-weight: 600;
    font-size: 10px; letter-spacing: 3px; color: var(--ink);
  }
  /* Front cover */
  .front { position: relative; width: 401px; height: 100%; overflow: hidden; }
  .front-photo-top {
    position: absolute; left: 0; top: 0; width: 100%; height: 281px;
    background: linear-gradient(180deg, var(--sky) 0%, var(--sky-light) 28%, var(--rock) 45%, var(--rock-dark) 70%, var(--sand) 100%);
  }
  .front-photo-bottom {
    position: absolute; left: 0; top: 367px; width: 100%; height: 236px;
    background: linear-gradient(180deg, var(--sand) 0%, #a24a22 55%, var(--sand-dark) 100%);
  }
  .front-title {
    position: absolute; left: 0; right: 0; top: 210px;
    text-align: center;
    font-family: "Bebas Neue", sans-serif; font-weight: 400; font-size: 60px; line-height: 1;
    color: var(--paper); text-shadow: 2px 3px 0 rgba(0,0,0,.35);
  }
  .subtitle-band {
    position: absolute; left: 0; top: 281px; width: 100%; height: 86px;
    background: var(--paper);
    display: flex; align-items: center; justify-content: center;
  }
  .subtitle {
    font-family: "Mulish", sans-serif; font-style: italic; font-weight: 500;
    font-size: 15px; line-height: 1.3; letter-spacing: 2.4px;
    color: var(--ink); text-align: center;
  }
  .front-author {
    position: absolute; left: 0; right: 0; top: 540px; text-align: center;
    font-family: "Oswald", sans-serif; font-weight: 600;
    font-size: 22px; letter-spacing: 12px; color: var(--paper);
  }
</style>
</head>
<body>
  <main class="spread">
    <section class="back">
      <div class="back-scene" role="img" aria-label="Night sky full of stars fading into dark red desert cliffs"></div>
      <h2 class="back-title"><span class="t1">THE</span><span class="t2">LANTERN</span><span class="t3">KEEPER</span></h2>
      <div class="blurb-disc">
        <p class="blurb">
          Lorem ipsum dolor sit<br>
          amet, consectetur adipiscing elit.<br>
          Quisque non odio vitae metus iaculis<br>
          aliquet in sed erat. Donec id lectus risus.<br>
          Proin non orci gravida, interdum odio non, dapi-<br>
          bus justo. Suspendisse aliquet lacus volutpat tortor<br>
          volutpat hendrerit. Etiam quis pharetra metus. Mae-<br>
          cenas finibus viverra mauris, at lacinia mi malesuada<br>
          in. Donec finibus, mauris non suscipit aliquet, neque ante<br>
          consequat nulla, et sodales orci neque vel mauris. Donec<br>
          auctor arcu quis malesuada euismod. Suspendisse sit<br>
          amet tempor leo, a tempus metus. Quisque porta semper<br>
          placerat. Proin nec condimentum sem. Cras dictum<br>
          pulvinar enim sed rutrum. Suspendisse commodo<br>
          sapien nec lacus accumsan semper. Nulla commo-<br>
          do, nisl eget pulvinar imperdiet, tellus tellus ul-<br>
          trices dui, ut imperdiet risus lorem ac ipsum.
        </p>
      </div>
    </section>

    <section class="spine">
      <span class="spine-title">THE LANTERN KEEPER</span>
      <span class="spine-author">MARISOL CRANE</span>
    </section>

    <section class="front">
      <div class="front-photo-top" role="img" aria-label="Red sandstone cliffs and rock towers under a starry blue sky"></div>
      <div class="front-photo-bottom" role="img" aria-label="Wide red desert floor with dry brush and a lone woman sitting on the ground"></div>
      <h1 class="front-title">THE LANTERN KEEPER</h1>
      <div class="subtitle-band">
        <p class="subtitle">Leave the Crooked Road That Runs<br>Past Every Open Gate<br>You Were Shown</p>
      </div>
      <p class="front-author">MARISOL CRANE</p>
    </section>
  </main>
</body>
</html>
```